stationary for pest control business
Brightwater Bug Control
stationary for pest control business - Environment
Creative Brief
Professional
Martin Kowalczyk
412 Birch Rd. Port Calloway, NY 11592
5164037281x7
martin@brightwaterbugctrl.com
http://brightwaterbugctrl.com/
need invoices, envelope, letterhead and business cards.
Free 2nd opinions, termite treatments and repairs. Over four generations serving Long Island.

```html
<!DOCTYPE html>
<html lang="en">
<head>
<meta charset="utf-8">
<title>Brightwater Bug Control — Business Cards</title>
<link href="https://fonts.googleapis.com/css2?family=Open+Sans:wght@400;600;700;800&display=swap" rel="stylesheet">
<style>
  :root {
    --bg: #e6e7ea;
    --navy: #0d2566;
    --navy-deep: #081845;
    --blue: #1d4fa8;
    --blue-light: #3f7fd0;
    --green: #6fae2c;
    --green-dark: #3f7d17;
    --ink: #2a2f3a;
    --grey: #6a6f7a;
    --white: #ffffff;
  }
  * { margin: 0; padding: 0; box-sizing: border-box; }
  html, body { width: 1200px; height: 901px; overflow: hidden; }
  body {
    background: var(--bg);
    font-family: "Open Sans", Arial, sans-serif;
    display: flex;
    align-items: center;
    justify-content: center;
    gap: 40px;
  }
  .card {
    position: relative;
    width: 540px;
    height: 309px;
    border-radius: 3px;
    overflow: hidden;
    box-shadow: 0 6px 18px rgba(0,0,0,0.18);
  }
  .card svg.art { position: absolute; inset: 0; width: 100%; height: 100%; }

  /* Back of card */
  .card-back {
    background: radial-gradient(ellipse at 45% 40%, var(--blue-light) 0%, var(--blue) 35%, var(--navy) 75%, var(--navy-deep) 100%);
  }
  .back-brand {
    position: absolute;
    left: 0; right: 0; top: 112px;
    display: flex; align-items: center; justify-content: center; gap: 12px;
  }
  .brand-dot {
    width: 38px; height: 38px; border-radius: 50%;
    background: var(--green);
    flex: none;
  }
  .brand-name {
    font-weight: 800;
    font-size: 25px;
    letter-spacing: -0.5px;
    line-height: 1;
  }
  .back-brand .brand-name { color: var(--white); }
  .back-url {
    position: absolute; left: 0; right: 0; top: 170px;
    text-align: center;
    color: var(--white);
    font-size: 12px;
    letter-spacing: 0.3px;
  }

  /* Front of card */
  .card-front { background: var(--white); }
  .front-brand {
    position: absolute; left: 26px; top: 58px;
    display: flex; align-items: center; gap: 10px;
  }
  .front-brand .brand-dot { width: 32px; height: 32px; }
  .front-brand .brand-name { color: var(--navy); font-size: 21px; }
  .holder-name {
    position: absolute; right: 26px; top: 22px;
    color: var(--blue);
    font-weight: 700;
    font-size: 14px;
  }
  .address {
    position: absolute; right: 26px; top: 98px;
    text-align: right;
    color: var(--grey);
    font-size: 11px;
    line-height: 16px;
  }
  .contact {
    position: absolute; right: 20px; top: 216px;
    list-style: none;
    text-align: right;
    color: var(--white);
    font-size: 11px;
    line-height: 17px;
  }
  .contact li { display: flex; align-items: center; justify-content: flex-end; gap: 8px; }
  .contact svg { width: 10px; height: 10px; flex: none; }
</style>
</head>
<body>

  <section class="card card-back" aria-label="Business card back">
    <div class="back-brand">
      <span class="brand-dot"></span>
      <span class="brand-name">Brightwater Bug Control</span>
    </div>
    <p class="back-url">www.brightwaterbugctrl.com</p>
  </section>

  <section class="card card-front" aria-label="Business card front">
    <svg class="art" viewBox="0 0 540 309" preserveAspectRatio="none" aria-hidden="true">
      <defs>
        <radialGradient id="frontBlue" cx="55%" cy="75%" r="70%">
          <stop offset="0" stop-color="#3f7fd0"/>
          <stop offset="0.45" stop-color="#1d4fa8"/>
          <stop offset="1" stop-color="#081845"/>
        </radialGradient>
        <linearGradient id="greenBand" x1="0" x2="1" y1="0" y2="0">
          <stop offset="0" stop-color="#3f7d17"/>
          <stop offset="0.5" stop-color="#8cc63f"/>
          <stop offset="1" stop-color="#3f7d17"/>
        </linearGradient>
      </defs>
      <path d="M0 172 C160 212 330 198 540 134 L540 309 L0 309 Z" fill="url(#greenBand)"/>
      <path d="M0 180 C160 220 330 206 540 142 L540 309 L0 309 Z" fill="#ffffff"/>
      <path d="M0 186 C160 226 330 212 540 148 L540 309 L0 309 Z" fill="#0d2566"/>
      <path d="M0 194 C160 236 330 222 540 158 L540 309 L0 309 Z" fill="url(#frontBlue)"/>
    </svg>

    <p class="holder-name">Martin Kowalczyk</p>
    <div class="front-brand">
      <span class="brand-dot"></span>
      <span class="brand-name">Brightwater Bug Control</span>
    </div>
    <p class="address">412 Birch Rd.<br>Port Calloway, NY 11592</p>
    <ul class="contact">
      <li>516 403 7281x7
        <svg viewBox="0 0 10 10"><path d="M2 1 L4 1 L4.6 3 L3.5 3.8 Q4.5 5.8 6.2 6.5 L7 5.4 L9 6 L9 8 Q5 9 2.2 6 Q0.8 4 2 1 Z" fill="#fff"/></svg>
      </li>
      <li>516 403 7290
        <svg viewBox="0 0 10 10"><rect x="1" y="3" width="8" height="5" rx="1" fill="#fff"/><rect x="3" y="1" width="4" height="2.5" fill="#fff"/></svg>
      </li>
      <li>martin@brightwaterbugctrl.com
        <svg viewBox="0 0 10 10"><rect x="0.8" y="2" width="8.4" height="6" fill="none" stroke="#fff" stroke-width="1"/><path d="M1 2.3 L5 5.5 L9 2.3" fill="none" stroke="#fff" stroke-width="1"/></svg>
      </li>
      <li>www.brightwaterbugctrl.com
        <svg viewBox="0 0 10 10"><circle cx="5" cy="5" r="4" fill="none" stroke="#fff" stroke-width="1"/><path d="M1 5 H9 M5 1 Q2.5 5 5 9 M5 1 Q7.5 5 5 9" fill="none" stroke="#fff" stroke-width="0.8"/></svg>
      </li>
    </ul>
  </section>

</body>
</html>
```